web site update

I want to get a better website for a small high end remodeling and construction company
I currently have a web site but you will find that it is not good.
www.pelbrookhaven.com
We are a high end construction / remodeling company that has been in business since 2003. We primarily work in the mid peninsula of the bay area. Most of our clientele are very educated captains of industry. This group is still the target client.
I had my logo designed by Vellum Forge a few years ago and I do like it, I like the orange and black or orange a blue. I don’t have a lot of content on hand as far as professional photographs.
Number of pages not sure and are open to: design pages vs full function website
I think what I am after is a web presence that will seal the deal as we are getting high referrals from past clients.
Construction
1 page

```html
<!DOCTYPE html>
<html lang="en">
<head>
<meta charset="utf-8">
<title>Pelbrook Haven Remodeling</title>
<link href="https://fonts.googleapis.com/css2?family=Lato:wght@400;700;900&display=swap" rel="stylesheet">
<style>
:root{
  --orange:#f26522;
  --ink:#111;
  --text:#333;
  --footer:#1b1b1b;
  --footer-bottom:#2a2a2a;
  --white:#fff;
}
*{box-sizing:border-box;margin:0;padding:0}
html,body{width:761px;height:1200px;overflow:hidden}
body{font-family:'Lato',sans-serif;color:var(--text);background:var(--white);position:relative}

/* header */
.site-header{position:absolute;left:0;top:0;width:761px;height:77px;background:var(--white);border-top:2px solid #999}
.brand{position:absolute;left:84px;top:16px;display:flex;align-items:center;gap:10px}
.brand-mark{width:40px;height:40px;background:var(--ink)}
.brand-name{font-weight:900;font-size:14px;line-height:16px;color:var(--orange);letter-spacing:.6px}
.callbar{position:absolute;right:82px;top:10px;font-size:11px;color:var(--orange);display:flex;align-items:center;gap:6px}
.callbar b{color:var(--ink);font-weight:700}
.nav{position:absolute;left:342px;top:52px;display:flex;gap:31px;font-size:9px;font-weight:700;color:var(--ink);letter-spacing:.3px}
.nav .active{color:var(--orange);position:relative}
.nav .active svg{position:absolute;left:-2px;top:-12px}

/* hero */
.hero{position:absolute;left:0;top:77px;width:761px;height:327px;
  background:linear-gradient(100deg,#3a1f14 0%,#6b3a24 12%,#a89a8c 24%,#e4e1dc 40%,#cfc9c0 52%,#7f8a6a 64%,#a7a58c 72%,#e6e4df 84%,#f2f1ee 100%)}
.hero-caption{position:absolute;left:84px;top:189px;width:310px;height:86px;background:rgba(25,25,25,.7)}
.hero-caption h1{position:absolute;left:13px;top:15px;color:var(--white);font-size:17px;line-height:25px;font-weight:900;white-space:nowrap}
.btn{position:absolute;display:flex;align-items:center;height:22px;background:var(--ink);color:var(--white);font-size:9px;font-weight:700;letter-spacing:.4px;padding:0 24px 0 11px;white-space:nowrap;text-decoration:none}
.btn .chev{position:absolute;right:-8px;top:3px;width:16px;height:16px;background:var(--orange);transform:rotate(45deg)}
.btn .chev::after{content:"»";position:absolute;transform:rotate(-45deg);left:4px;top:-1px;font-size:12px;color:var(--white)}
.dots{position:absolute;left:95px;top:303px;display:flex;gap:8px}
.dots span{width:9px;height:9px;border:1.5px solid var(--white);border-radius:50%}
.dots span:first-child{border-color:var(--orange)}

/* welcome */
.welcome{position:absolute;left:0;top:404px;width:761px;height:231px;background:linear-gradient(100deg,#ececec,#fafafa 50%,#ededed)}
.roof{position:absolute;left:50%;transform:translateX(-50%)}
.section-title{position:absolute;width:100%;text-align:center;font-size:18px;font-weight:900;color:var(--ink)}
.section-title em{font-style:normal;color:var(--orange)}
.welcome p{position:absolute;left:93px;top:97px;width:575px;text-align:center;font-size:9.2px;line-height:15.3px;color:var(--ink)}

/* services */
.card{position:absolute;top:732px;width:178px;height:202px;border:1px solid #ccc;background:var(--white)}
.card .photo{height:95px}
.card h3{margin-top:14px;text-align:center;color:var(--orange);font-size:11.5px;font-weight:700;letter-spacing:.4px}
.card p{margin-top:9px;text-align:center;font-size:9px;line-height:15.3px;color:var(--text);padding:0 12px}

/* footer */
.site-footer{position:absolute;left:0;top:985px;width:761px;height:185px;background:var(--footer);border-top:2px solid var(--orange);color:#ddd}
.f-head{position:absolute;top:20px;font-size:9.5px;font-weight:700;color:var(--white);letter-spacing:.3px;padding-bottom:8px;border-bottom:1px dashed #555}
.links{position:absolute;left:84px;top:48px;width:74px;list-style:none}
.links li{font-size:8px;height:26px;line-height:26px;border-bottom:1px solid #333;padding-left:11px;position:relative}
.links li:last-child{border-bottom:0}
.links li::before{content:"";position:absolute;left:0;top:11px;width:3px;height:3px;background:var(--orange)}
.field{position:absolute;left:190px;width:124px;background:var(--white);color:#666;font-size:7px;font-style:italic;padding:3px 0 0 20px}
.submit{position:absolute;left:190px;top:148px;width:51px;height:19px;background:var(--orange);color:var(--white);font-size:8.5px;font-weight:700;text-align:center;line-height:19px}
.map{position:absolute;left:349px;top:52px;width:142px;height:52px;background:linear-gradient(#a9c6e0,#d8cf9e);border:2px solid #6a7f95}
.ci{position:absolute;left:349px;font-size:7.5px;color:var(--white);display:flex;gap:8px;line-height:10px}
.f-brand{position:absolute;left:525px;top:52px;display:flex;align-items:center;gap:10px}
.f-brand .brand-mark{background:var(--white)}
.f-brand .brand-name{color:#ccc}
.social{position:absolute;left:524px;top:120px;display:flex;gap:11px}
.social span{width:21px;height:21px;border-radius:3px}
.copyright{position:absolute;left:0;top:1170px;width:761px;height:30px;background:var(--footer-bottom);color:#ccc;font-size:8px;text-align:center;line-height:30px}
</style>
</head>
<body>

<header class="site-header">
  <div class="brand">
    <span class="brand-mark"></span>
    <span class="brand-name">PELBROOK HAVEN<br>REMODELING</span>
  </div>
  <div class="callbar">
    <svg width="14" height="14" viewBox="0 0 24 24" fill="none" stroke="#555" stroke-width="1.6"><path d="M5 3l4 1 1 5-2 1a12 12 0 0 0 6 6l1-2 5 1 1 4c-1 2-3 2-4 2A17 17 0 0 1 3 7c0-1 0-3 2-4z"/></svg>
    CALL US NOW! : <b>415.555.0148</b>
    <svg width="16" height="12" viewBox="0 0 16 12" fill="none" stroke="#111" stroke-width="1.3" style="margin-left:10px"><rect x="1" y="1" width="14" height="10"/><path d="M1 1l7 6 7-6"/></svg>
  </div>
  <nav class="nav">
    <span class="active"><svg width="34" height="10" viewBox="0 0 34 10"><path d="M1 9L17 1l16 8" fill="none" stroke="#111" stroke-width="1.6"/></svg>HOME</span>
    <span>ABOUT US</span><span>SERVICES</span><span>GALLERY</span><span>CONTACT US</span>
  </nav>
</header>

<section class="hero" role="img" aria-label="Photo of a remodeled kitchen with cherry cabinets, white counters, a mosaic backsplash and a window onto green hills">
  <div class="hero-caption">
    <h1>A QUALITY LINE OF REMODELING &amp;<br>CONSTRUCTION SERVICES</h1>
  </div>
  <a class="btn" style="left:95px;top:262px">CALL US TODAY<span class="chev"></span></a>
  <div class="dots"><span></span><span></span><span></span></div>
</section>

<section class="welcome">
  <svg class="roof" style="top:29px" width="74" height="24" viewBox="0 0 74 24"><path d="M1 23L37 2l36 21" fill="none" stroke="#111" stroke-width="2.5"/></svg>
  <h2 class="section-title" style="top:56px">WELCOME TO <em>PELBROOK HAVEN</em> REMODELING</h2>
  <p>Lorem ipsum dolor sit amet, consectetuer adipiscing elit, sed diam nonummy nibh euismod tincidunt ut laoreet dolore magna aliquam erat volutpat. Ut wisi enim ad minim veniam, quis nostrud exerci tation ullamcorper suscipit lobortis nisl ut aliquip ex ea commodo consequat sit Duis autem vel eum iriure dolor in hendrerit in vulputate velit esse molestie consequat, vel illum dolore eu feugiat nulla facilisis at vero eros accumsan et iusto odio dignissim qui blandit praesent luptatum zzril delenit augue duis dolore te feugait nulla facilisi.</p>
  <a class="btn" style="left:335px;top:172px">READ MORE<span class="chev"></span></a>
</section>

<section class="services">
  <svg class="roof" style="top:665px" width="66" height="22" viewBox="0 0 66 22"><path d="M1 21L33 2l32 19" fill="none" stroke="#111" stroke-width="2.5"/></svg>
  <h2 class="section-title" style="top:691px">OUR <em>SERVICES</em></h2>

  <article class="card" style="left:84px">
    <div class="photo" role="img" aria-label="Photo of a white kitchen with bar stools at an island" style="background:linear-gradient(160deg,#5a4f46 0%,#b9b2a8 35%,#e9e6e1 60%,#7d6d60 100%)"></div>
    <h3>KITCHEN REMODELING</h3>
    <p>Lorem ipsum dolor sit amet sit almet consectetuer adipiscing elit, sed diam nonummy nibh euismod tinci</p>
  </article>
  <a class="btn" style="left:126px;top:923px">READ MORE<span class="chev"></span></a>

  <article class="card" style="left:292px">
    <div class="photo" role="img" aria-label="Photo of a bathroom vanity with blue and white tiles" style="background:linear-gradient(170deg,#3d4a7e 0%,#8a94c0 35%,#dcdde6 60%,#c9c8cc 100%)"></div>
    <h3>BATHROOM RENOVATION</h3>
    <p>Lorem ipsum dolor sit amet sit almet consectetuer adipiscing elit, sed diam nonummy nibh euismod tinci</p>
  </article>
  <a class="btn" style="left:333px;top:923px">READ MORE<span class="chev"></span></a>

  <article class="card" style="left:500px">
    <div class="photo" role="img" aria-label="Photo of a custom home among tall trees" style="background:linear-gradient(180deg,#9aa3a6 0%,#6f7a6a 40%,#b59a7a 62%,#4d4a2e 100%)"></div>
    <h3>CUSTOM HOMES</h3>
    <p>Lorem ipsum dolor sit amet sit almet consectetuer adipiscing elit, sed diam nonummy nibh euismod tinci</p>
  </article>
  <a class="btn" style="left:541px;top:923px">READ MORE<span class="chev"></span></a>
</section>

<footer class="site-footer">
  <h4 class="f-head" style="left:84px;width:74px">QUICK LINKS</h4>
  <ul class="links"><li>HOME</li><li>ABOUT US</li><li>SERVICES</li><li>GALLERY</li><li>CONTACT US</li></ul>

  <h4 class="f-head" style="left:190px;width:126px">QUICK INQUIRY</h4>
  <div class="field" style="top:52px;height:16px">Name</div>
  <div class="field" style="top:72px;height:16px">Email</div>
  <div class="field" style="top:95px;height:42px">Message</div>
  <div class="submit">SUBMIT</div>

  <h4 class="f-head" style="left:349px;width:142px">CONTACT INFORMATION</h4>
  <div class="map" role="img" aria-label="Map showing the office location"></div>
  <div class="ci" style="top:113px">
    <svg width="8" height="11" viewBox="0 0 8 11"><path d="M4 11L1 5a3 3 0 1 1 6 0z" fill="#fff"/><circle cx="4" cy="4" r="1.2" fill="#1b1b1b"/></svg>
    <span>123 Sed diam nonmy nibh euod<br>tinc dunt ut laoreet</span>
  </div>
  <div class="ci" style="top:142px;font-size:8.5px;font-weight:700">
    <svg width="9" height="9" viewBox="0 0 9 9"><path d="M1 8C1 4 4 1 8 1" fill="none" stroke="#fff" stroke-width="2"/></svg>415.555.0148
  </div>
  <div class="ci" style="top:162px;font-weight:700">
    <svg width="10" height="8" viewBox="0 0 10 8" fill="none" stroke="#fff"><rect x=".5" y=".5" width="9" height="7"/><path d="M.5 .5l4.5 4 4.5-4"/></svg>hello@pelbrookhaven.com
  </div>

  <div class="f-brand">
    <span class="brand-mark"></span>
    <span class="brand-name">PELBROOK HAVEN<br>REMODELING</span>
  </div>
  <div class="social" aria-label="Social media links">
    <span style="background:#3b5b98"></span>
    <span style="background:#3ba9e0"></span>
    <span style="background:#1f6fa8"></span>
    <span style="background:#d1472f"></span>
    <span style="background:#6b8aa6"></span>
  </div>
</footer>
<div class="copyright">© COPYRIGHT 2016 PELBROOK HAVEN REMODELING. ALL RIGHT RESERVED.</div>

</body>
</html>
```